Restaurant Menu Design

An A3 and A4 template in MS publisher or something similar that will allow copy and paste editing of menu items. Approx 20 lines of menu choices and double sided

```html
<!DOCTYPE html>
<html lang="en">
<head>
<meta charset="utf-8">
<title>The Harbour Gate Hotel – Menu</title>
<link href="https://fonts.googleapis.com/css2?family=Montserrat:wght@400;500;600;700;800&display=swap" rel="stylesheet">
<style>
:root{
  --gold:#d9b043;
  --gold-soft:#e6c46a;
  --ink:#1f1d1d;
  --band:#2a2727;
  --paper:#ffffff;
  --backdrop:#ececec;
  --muted:#444;
  --green:#8cc63f;
  --badge-dark:#3a6f4a;
}
*{box-sizing:border-box;margin:0;padding:0}
html,body{width:1200px;height:3561px;overflow:hidden}
body{background:var(--backdrop);font-family:"Montserrat",Arial,sans-serif;color:var(--ink);position:relative}
.sheet{position:absolute;left:253px;width:694px;height:984px;background:var(--paper);box-shadow:0 2px 6px rgba(0,0,0,.06)}
.sheet--front{top:1197px}
.sheet--back{top:2264px}

.masthead{height:178px;background:var(--band);position:relative;padding:26px 63px}
.masthead__title{color:var(--gold);font-weight:700;font-size:31px;letter-spacing:-.2px}
.masthead__allergens-title{color:var(--gold);font-weight:600;font-size:11px;margin-top:8px}
.allergen-list{display:grid;grid-template-columns:158px 142px 150px;color:#e9e9e9;font-size:8px;line-height:11px;margin-top:4px}
.brandmark{position:absolute;right:42px;top:28px;width:128px;height:128px;display:flex;flex-direction:column;align-items:center;justify-content:center;gap:8px}
.brandmark__dot{width:46px;height:46px;border-radius:50%;background:var(--gold)}
.brandmark__name{color:var(--gold);font-weight:700;font-size:11px;text-align:center;line-height:13px}

.menu{padding:24px 55px 0 63px}
.sheet--back .menu{padding-top:36px}
.section-head{display:flex;align-items:center;gap:14px;color:var(--gold);font-weight:700;font-size:18.5px;margin:0 0 12px;letter-spacing:-.2px}
.section-head::after{content:"";flex:1;height:1.2px;background:var(--gold)}
.section-head--spaced{margin-top:18px}
.item{display:grid;grid-template-columns:399px 128px 1fr;font-size:10.4px;line-height:14px;margin-bottom:11.5px}
.item__name{font-weight:700}
.item__desc{font-weight:400;color:var(--muted)}
.item__allergens{font-weight:400;color:var(--muted)}
.item__price{font-weight:700}
.sandwich-head{font-weight:800;font-size:16.5px;margin:22px 0 10px;letter-spacing:-.2px}

.sides{position:relative;border-top:1.2px solid var(--gold);margin-top:10px;display:grid;grid-template-columns:284px 1fr;padding-top:12px}
.sides__tab{position:absolute;left:0;top:-1px;background:var(--gold);color:var(--ink);font-weight:700;font-size:12px;padding:1px 10px 1px 14px}
.sides__col{display:grid;grid-template-columns:142px 80px 1fr;font-size:10.4px;line-height:14.5px;font-weight:700;padding-top:12px}
.sides__col--right{border-left:1.2px solid var(--gold);padding-left:32px;padding-top:0;grid-template-columns:145px 80px 1fr}
.sides__col span:nth-child(3n+2){font-weight:400;color:var(--muted)}

.footer-bar{position:absolute;left:63px;right:47px;height:25px;background:var(--gold);display:flex;align-items:center;justify-content:space-between}
.sheet--front .footer-bar{top:936px}
.sheet--back .footer-bar{top:933px}
.footer-bar__wifi{height:100%;width:225px;background:var(--paper);clip-path:polygon(0 0,100% 0,91% 100%,0 100%);display:flex;align-items:center;padding-left:18px;font-size:11.5px;font-weight:500;border-left:1.5px solid var(--gold);border-top:1.5px solid var(--gold);border-bottom:1.5px solid var(--gold)}
.footer-bar__wifi::after{content:"";width:1px;height:13px;background:var(--ink);margin-left:12px}
.footer-bar__name{font-weight:700;font-size:10.5px;letter-spacing:2.4px;padding-right:14px}
.footer-bar__badges{display:flex;align-items:center;gap:8px;padding-right:14px}
.badge-round{width:16px;height:16px;border-radius:50%;background:var(--badge-dark)}
.badge-rating{width:84px;height:34px;background:var(--green);border-radius:3px;margin-top:-12px}
.badge-note{width:70px;height:10px;background:var(--gold-soft);border-radius:2px}
</style>
</head>
<body>

<article class="sheet sheet--front">
  <header class="masthead">
    <h1 class="masthead__title">The Harbour Gate Hotel</h1>
    <p class="masthead__allergens-title">Allergens (In Brackets):</p>
    <div class="allergen-list">
      <div>1. Gluten containing cereals<br>2. Crustaceans<br>3. Molluscs<br>4. Fish<br>5. Peanuts</div>
      <div>6. Lupin<br>7. Tree Nuts<br>8. Soya<br>9. Eggs<br>10. Milk<br>11. Celery</div>
      <div>12. Mustard<br>13. Sesame<br>14. Sulphur dioxide<br>(V) = Vegetarian<br>(VG) = Vegan Friendly</div>
    </div>
    <div class="brandmark"><span class="brandmark__dot"></span><span class="brandmark__name">The Harbour Gate Hotel</span></div>
  </header>

  <section class="menu">
    <h2 class="section-head">STARTERS</h2>
    <div class="item"><div><div class="item__name">Soup of The Day (v)</div><div class="item__desc">Fresh artisan baguette</div></div><div class="item__allergens">(1. 10. 12. 14)</div><div class="item__price">£7</div></div>
    <div class="item"><div><div class="item__name">Crispy Duck Salad (v)</div><div class="item__desc">Spring onions, ginger, chilli, bean sprouts,<br>sesame seeds, hoisin sauce</div></div><div class="item__allergens">(3. 5. 8. 13 .14)</div><div class="item__price">£9</div></div>
    <div class="item"><div><div class="item__name">Arancini Balls (v)</div><div class="item__desc">Stuffed with tomato, shallot, basil &amp; mozzarella, smoked tomato<br>beurre blanc sauce</div></div><div class="item__allergens">(1.9.10.14)</div><div class="item__price">£8</div></div>
    <div class="item"><div><div class="item__name">Deep Fried Breaded Chicken Strips</div><div class="item__desc">Sweet chilli mayonnaise</div></div><div class="item__allergens">(1. 10 .11. 12. 13. 14)</div><div class="item__price">£8.5</div></div>
    <div class="item"><div><div class="item__name">Salt &amp; Pepper Squid</div><div class="item__desc">Fresh chilli, ginger, spring onion, salad garnish, sweet chilli sauce</div></div><div class="item__allergens">(1. 3)</div><div class="item__price">£8.5</div></div>
    <div class="item"><div><div class="item__name">Smoked Mackerel</div><div class="item__desc">Apple, beetroot &amp; new potato salad, pickled radish &amp; carrot garnish</div></div><div class="item__allergens">(4. 9. 14)</div><div class="item__price">£8.5</div></div>

    <h2 class="section-head section-head--spaced">DAILY SPECIALS</h2>
    <div class="item"><div><div class="item__name">8oz Dry Aged Ribeye Steak</div><div class="item__desc">Served with chips, house salad, field mushroom,<br>tomato &amp; a choice of blue cheese or peppercorn sauce</div></div><div class="item__allergens">(10. 11. 12. 14)</div><div class="item__price">£29.5</div></div>
    <div class="item"><div><div class="item__name">Harbourside Battered Fish &amp; Chips</div><div class="item__desc">Fresh cod, buttered petit pois, tartare sauce &amp; lemon</div></div><div class="item__allergens">(1. 4. 9. 10. 14)</div><div class="item__price">£15</div></div>
    <div class="item"><div><div class="item__name">Chef's Homemade Pie Of The Day</div><div class="item__desc">Buttery mash, seasonal vegetables &amp; jus</div></div><div class="item__allergens">(1. 10. 11. 12. 14)</div><div class="item__price">£16</div></div>
    <div class="item"><div><div class="item__name">Gourmet Cheeseburger</div><div class="item__desc">8oz steak burger, toasted opulent bun, lettuce, Swiss cheese, tomato,<br>pickled gherkin, caramelized onion, chips &amp; onion rings Choose either<br>peppercorn mayo sauce or hot chilli sauce</div></div><div class="item__allergens">(1. 9. 10. 11. 12. 14)</div><div class="item__price">£16</div></div>
    <div class="item"><div><div class="item__name">Honey Roast Ham</div><div class="item__desc">2 eggs, chips, buttered petit pois</div></div><div class="item__allergens">(9. 10)</div><div class="item__price">£15</div></div>
    <div class="item"><div><div class="item__name">Battered Chicken Fillet Burger</div><div class="item__desc">Gem lettuce, tomato, gherkin, crispy onions, teriyaki sauce,<br>chips, onion rings</div></div><div class="item__allergens">(1. 8. 10. 13. 14)</div><div class="item__price">£15.5</div></div>
    <div class="item"><div><div class="item__name">Sea Bass Fillet</div><div class="item__desc">Steamed white rice, vegetable stir fry, Thai broth, chilli, ginger,<br>spring onion micro salad</div></div><div class="item__allergens">(4. 8. 13)</div><div class="item__price">£19</div></div>
    <div class="item"><div><div class="item__name">Breaded Scampi</div><div class="item__desc">Chips &amp; buttered petit pois</div></div><div class="item__allergens">(1. 2. 10)</div><div class="item__price">£14.5</div></div>
  </section>

  <footer class="footer-bar"><span class="footer-bar__wifi">WIFI CODE</span><span class="footer-bar__name">THE HARBOUR GATE HOTEL</span></footer>
</article>

<article class="sheet sheet--back">
  <section class="menu">
    <h2 class="section-head">PUDDINGS</h2>
    <div class="item"><div><div class="item__name">Homemade Sticky Toffee Pudding (v)</div><div class="item__desc">Bourbon sauce, vanilla ice cream &amp; fudge pieces</div></div><div class="item__allergens">(1. 9. 10)</div><div class="item__price">£8</div></div>
    <div class="item"><div><div class="item__name">Selection of Cheeses</div><div class="item__desc">Aged farmhouse cheddar, creamy blue &amp; soft ripened brie,<br>onion marmalade, quince, celery, candied walnuts &amp; savoury biscuits</div></div><div class="item__allergens">(1. 7. 10. 11. 12. 14)</div><div class="item__price">£9.95</div></div>
    <div class="item"><div><div class="item__name">Chocolate Brownie (v)</div><div class="item__desc">chocolate sauce &amp; vanilla ice cream</div></div><div class="item__allergens">(1. 9. 10)</div><div class="item__price">£8</div></div>
    <div class="item"><div><div class="item__name">Orange Posset (v)</div><div class="item__desc">mini almond short bread biscuits, passion fruit coulis</div></div><div class="item__allergens">(1. 7. 9. 10. 14)</div><div class="item__price">£8</div></div>
    <div class="item"><div><div class="item__name">Cheesecake of the Day</div><div class="item__desc">(Please Ask) Ice cream</div></div><div class="item__allergens">-</div><div class="item__price">£8</div></div>
    <div class="item"><div><div class="item__name">Strawberries &amp; Cream Mille Feuille</div><div class="item__desc">Ginger, hazelnut crumb &amp; strawberry ice cream</div></div><div class="item__allergens">(1. 10. 14)</div><div class="item__price">£9</div></div>
    <div class="item"><div><div class="item__name">Toffee Fudge &amp; Brownie Sundae<br>Knickerbocker Glory Sundae<br>Ice Cream (v)</div><div class="item__desc">2 scoops – chocolate, vanilla, pistachio (7), salted caramel (7) or strawberry</div></div><div class="item__allergens">(1. 9. 10)<br>(9. 10)<br>(1. 9. 10)</div><div class="item__price">£9<br>£9.5<br>£8</div></div>

    <h2 class="section-head section-head--spaced">VEGAN STARTERS</h2>
    <div class="item"><div><div class="item__name">Maple-Roasted Carrot Soup</div><div class="item__desc">Ginger &amp; coriander infusion, fresh crispy bread</div></div><div class="item__allergens">(1. 11)</div><div class="item__price">£7</div></div>
    <div class="item"><div><div class="item__name">Bread &amp; Marinated Olives</div><div class="item__desc">Fresh bread, marinated olives &amp; balsamic olive oil</div></div><div class="item__allergens">(1. 8. 14)</div><div class="item__price">£7</div></div>

    <h2 class="section-head section-head--spaced">VEGAN MAINS</h2>
    <div class="item"><div><div class="item__name">Gourmet Green Ridge Vegan Burger</div><div class="item__desc">vegan cheese, chipotle aioli sauce, lettuce &amp; tomato, chips</div></div><div class="item__allergens">(1. 14)</div><div class="item__price">£15.5</div></div>
    <div class="item"><div><div class="item__name">Vegan Chilli Con Carne</div><div class="item__desc">Steamed white rice, smashed avocado, crispy tortilla chips,<br>micro herb garnish</div></div><div class="item__allergens">(8.11. 14)</div><div class="item__price">£15</div></div>

    <h2 class="section-head section-head--spaced">VEGAN PUDDING</h2>
    <div class="item"><div><div class="item__name">Vegan Belgian Sweet Waffles</div><div class="item__desc">Vegan vanilla, Pistachio Crumb, Passion Fruits Coulis</div></div><div class="item__allergens">(1)</div><div class="item__price">£8.5</div></div>

    <h2 class="sandwich-head">MADE TO ORDER SANDWICHES ON WHITE OR GRANARY BREAD</h2>
    <div class="item"><div class="item__name">Ham &amp; Tomato<br>Prawns &amp; Marie Rose Sauce, Lettuce<br>Butchers Pork &amp; Leek Sausage, Caramelised Onion<br>Cheese &amp; Apple &amp; Date Chutney</div><div class="item__allergens">(1)<br>(1. 10. 11. 14)<br>(1.10. 14)<br>(1. 10. 12. 14)</div><div class="item__price">£8<br>£8.5<br>£8.5<br>£8</div></div>

    <div class="sides">
      <span class="sides__tab">SIDES</span>
      <div class="sides__col">
        <span>Chips</span><span>(1)</span><span>£4.5</span>
        <span>Chips &amp; Cheese</span><span>(1. 10)</span><span>£5.5</span>
        <span>Seasonal Vegetables</span><span>(10)</span><span>£3.95</span>
        <span>House Salad</span><span>(12. 14)</span><span>£3.95</span>
        <span>Garlic Bread</span><span>(1)</span><span>£5.25</span>
      </div>
      <div class="sides__col sides__col--right">
        <span>Garlic Bread &amp; Cheese</span><span>(1)</span><span>£6.5</span>
        <span>Olives</span><span>(1. 10)</span><span>£4</span>
        <span>Bread &amp; Oil</span><span>(1)</span><span>£4.95</span>
        <span>Onion Rings</span><span>(1)</span><span>£4.5</span>
      </div>
    </div>
  </section>

  <footer class="footer-bar"><span class="footer-bar__wifi">WIFI CODE</span>
    <span class="footer-bar__badges"><span class="badge-round" role="img" aria-label="Food safety partner badge"></span><span class="badge-rating" role="img" aria-label="Food hygiene rating badge"></span><span class="badge-note"></span></span>
  </footer>
</article>

</body>
</html>
```